Wordpress Redesign Project

Our website needs to become amazing. Because now it's not. The homepage especially does not actively convey what we do in an elegant way. We would want a minimalist redesign of www.plorvex.com to look more like:

http://brennocraft.com/
http://www.volarin.com/en-us/volarinkestro.html
http://www.umba.com/

It needs to work on Wordpress and be easily uploaded.

We also need an inside page of case studies (currently http://www.plorvex.com/social-media-clients/) that plays the video in a larger pop-up screen .

Target Market(s)

Social Media Professionals, Creative and Advertising Agencies, Event marketing professionals

Industry/Entity Type

Media

```html
<!DOCTYPE html>
<html lang="en">
<head>
<meta charset="utf-8">
<title>plorvex – Creating Brand Champions</title>
<link rel="stylesheet" href="https://fonts.googleapis.com/css2?family=Yanone+Kaffeesatz:wght@400;600&family=Arimo:wght@400&display=swap">
<style>
:root{
  --pink:#d9188a;
  --pink-dark:#b80f72;
  --pink-soft:#e43a9d;
  --bg:#efefef;
  --card:#ffffff;
  --text:#333333;
  --muted:#555555;
  --rule:#dddddd;
}
*{box-sizing:border-box;margin:0;padding:0}
html,body{width:1091px;height:1200px;overflow:hidden}
body{background:var(--bg);font-family:'Arimo',Arial,sans-serif;color:var(--text);position:relative}
.abs{position:absolute}
.heading{font-family:'Yanone Kaffeesatz',sans-serif;font-weight:400;color:var(--pink);text-transform:uppercase}
.backdrop{position:absolute;left:0;top:0}
.logo{left:192px;top:8px;display:flex;align-items:center;gap:6px}
.logo-mark{width:56px;height:56px;border-radius:50%;background:var(--pink)}
.logo-name{font-family:'Yanone Kaffeesatz',sans-serif;font-weight:600;font-size:34px;color:var(--pink)}
.tagline{left:328px;top:28px;font-size:19px;letter-spacing:1px}
.demo{left:780px;top:0;width:116px;height:18px}
.demo span{position:absolute;left:0;right:0;top:2px;text-align:center;font-family:'Yanone Kaffeesatz',sans-serif;font-size:11px;color:var(--pink)}
.nav{right:219px;top:52px;display:flex;gap:7px;font-family:'Yanone Kaffeesatz',sans-serif;font-size:12.5px;color:#fff;text-transform:uppercase}
.nav i{font-style:normal}
.hero{left:196px;top:77px;width:699px;height:280px}
.hero-caption{background:var(--pink);color:#fff;font-family:'Yanone Kaffeesatz',sans-serif;font-size:13.5px;text-transform:uppercase;padding:5px 15px;white-space:nowrap}
.cap1{left:535px;top:185px;width:335px}
.cap2{left:676px;top:216px;width:194px}
.card{background:var(--card);border-radius:3px;box-shadow:0 1px 6px rgba(0,0,0,.08)}
.what{left:196px;top:378px;width:699px;height:262px}
.what h2{position:absolute;left:15px;top:13px;font-size:14px}
.what .thumb{position:absolute;left:16px;top:40px;width:105px;height:82px;background:linear-gradient(135deg,#222 40%,#7a1b5a 70%,#c52a8c)}
.what p{position:absolute;left:136px;top:40px;width:540px;font-size:9.2px;line-height:13px;color:var(--muted)}
.tiles{position:absolute;left:0;top:140px;width:699px;display:flex}
.tile{width:174.75px}
.tile .img{height:94px}
.tile .label{height:28px;background:var(--pink-dark);color:#fff;font-family:'Yanone Kaffeesatz',sans-serif;font-size:11px;text-align:center;line-height:28px;text-transform:uppercase;border-right:1px solid #a30c64}
.tile.active .label{background:var(--pink)}
.story{left:196px;top:660px;width:460px}
.story h3{font-size:13.2px}
.story p{margin-top:6px;font-size:9.3px;line-height:13px;color:var(--muted)}
.story a{color:var(--pink);text-decoration:none}
.video{left:196px;top:745px;width:219px;height:160px;background:#111}
.video .frame{position:absolute;left:0;top:16px;width:219px;height:124px;background:linear-gradient(120deg,#4a5680,#a08a86 55%,#cdb9a8)}
.why{left:435px;top:745px;width:219px;height:160px;padding:12px 15px}
.why h3{font-size:12.5px}
.why p{margin-top:2px;font-size:9.1px;line-height:13px;color:var(--muted)}
.blog{left:676px;top:656px;width:219px;height:249px;padding:12px 16px}
.blog h3{font-size:13px;margin-left:16px}
.blog ul{list-style:none;margin-top:10px}
.blog li{position:relative;padding:0 0 8px 16px;margin-bottom:8px;border-bottom:1px solid var(--rule);font-size:8.9px;line-height:13px;color:var(--muted)}
.blog li:last-child{border-bottom:0}
.blog li.current{color:var(--pink)}
.blog li::before{content:"›";position:absolute;left:0;top:-3px;font-size:15px;font-weight:bold;color:#222}
.blog li.current::before{color:var(--pink)}
.divider{left:196px;width:699px;height:1px;background:var(--rule)}
.clients{left:196px;top:933px;display:flex;gap:9px}
.client{width:102px;height:62px;background:#fff;border:3px solid #dcdcdc;border-radius:4px;display:flex;align-items:center;justify-content:center;font-family:'Yanone Kaffeesatz',sans-serif;font-size:19px;color:#555}
.pager{left:636px;top:942px;width:19px;height:19px;background:var(--pink)}
.pager.prev{top:965px;background:#222}
.cta{left:676px;top:933px;width:219px;height:61px;background:linear-gradient(#e5289a,var(--pink-dark));border-radius:3px;color:#fff;font-family:'Yanone Kaffeesatz',sans-serif;font-size:13.5px;line-height:16px;padding:14px 0 0 35px;text-transform:uppercase}
.foot h4{font-family:'Arimo',Arial,sans-serif;font-weight:400;font-size:11.5px;color:var(--pink);text-transform:uppercase}
.foot ul{list-style:none;margin-top:8px}
.foot li{font-size:9.2px;color:var(--muted);line-height:17.5px;padding-left:13px;position:relative}
.foot li::before{content:"›";position:absolute;left:0;top:-1px;font-size:13px;font-weight:bold;color:#222}
.foot.follow li{padding-left:26px;line-height:19.5px}
.foot.follow li::before{content:"";width:14px;height:14px;top:3px;background:#888;border-radius:2px}
.foot p{margin-top:8px;font-size:9.2px;line-height:13px;color:var(--muted)}
.footer-bar{left:0;top:1160px;width:1091px;height:40px;background:var(--pink);color:#fff;font-size:9.2px;padding:14px 0 0 196px}
</style>
</head>
<body>
<svg class="backdrop" width="1091" height="420" aria-hidden="true">
  <polygon points="624,0 1091,0 1091,420 0,420 0,358 192,250 192,74 500,74" fill="#d9188a"/>
</svg>

<div class="abs logo"><span class="logo-mark"></span><span class="logo-name">plorvex</span></div>
<div class="abs heading tagline">Creating Brand Champions</div>

<div class="abs demo">
  <svg width="116" height="18" aria-hidden="true"><polygon points="0,18 18,0 116,0 98,18" fill="#fff"/></svg>
  <span>REQUEST A DEMO</span>
</div>

<nav class="abs nav">
  <span>About Us</span><i>•</i><span>Solutions</span><i>•</i><span>News</span><i>•</i><span>Resource</span><i>•</i><span>Our Work</span><i>•</i><span>Social Blog</span>
</nav>

<svg class="abs hero" viewBox="0 0 699 280">
  <defs>
    <linearGradient id="heroTone" x1="0" y1="0" x2="1" y2="1">
      <stop offset="0" stop-color="#d8dde4"/><stop offset=".45" stop-color="#7b7f88"/><stop offset="1" stop-color="#2c2f36"/>
    </linearGradient>
  </defs>
  <polygon points="0,0 699,0 699,218 580,280 0,280" fill="#fff"/>
  <polygon points="5,5 694,5 694,214 578,275 5,275" fill="url(#heroTone)" role="img" aria-label="Photo of a business team gathered around a laptop in a meeting"/>
  <path d="M677 252 l-6 7 6 7 M684 252 l6 7 -6 7" stroke="#fff" stroke-width="1.8" fill="none"/>
</svg>
<div class="abs hero-caption cap1">Lorem Ipsum is simply dummy text of the printing and typesetti</div>
<div class="abs hero-caption cap2">Printing and typesetting industry.</div>

<section class="abs card what">
  <h2 class="heading">What we do</h2>
  <div class="thumb" role="img" aria-label="Photo of an Altavane car brand display"></div>
  <p>plorvex is in the business of creating brand champions. We help get consumers to put your branded content into their Linkora News Feed and Chirply stream while attending live events. It is product placement in social media and the most scalable form of word-of-mouth advertising. We facilitate the posts by providing a platform that connects to photobooths, roving photographers, Like boxes, games and buzz walls and generates automated social media posts. It is a significant leverage on event guest engagement, drives social media impressions and extends the brand's audience.</p>
  <svg class="abs" style="left:644px;top:90px" width="40" height="40" aria-hidden="true"><polygon points="40,0 40,40 0,40" fill="#d9188a"/><path d="M28 25v12M22 31h12" stroke="#fff" stroke-width="1.6"/></svg>
  <div class="tiles">
    <div class="tile active"><div class="img" role="img" aria-label="Photo of costumed guests at a branded event photobooth" style="background:linear-gradient(135deg,#7aa7d6,#c06050 60%,#5a6a3a)"></div><div class="label">Amplify your events</div></div>
    <div class="tile"><div class="img" role="img" aria-label="Black and white photo of skiers at a mountain venue" style="background:linear-gradient(#c8c8c8,#777 60%,#aaa)"></div><div class="label">Connect venues</div></div>
    <div class="tile"><div class="img" role="img" aria-label="Black and white photo of a cheering crowd" style="background:linear-gradient(135deg,#555,#999 50%,#333)"></div><div class="label">In action</div></div>
    <div class="tile"><div class="img" role="img" aria-label="Black and white photo of friends celebrating together" style="background:linear-gradient(135deg,#333,#888 50%,#222)"></div><div class="label">Social solutions</div></div>
  </div>
</section>

<section class="abs story">
  <h3 class="heading">Altavane amplifies Grand Prix Series with RFID using social media technology</h3>
  <p>The video below shows how auto brands are connecting auto show and lifestyle event guests directly to social media using RFID and NFC Technology. These activations are fun for guests and expand the potential audience for social engagement beyond attendees to include their social network friends.<br><a>Watch Video Below to see it in action!</a></p>
</section>

<div class="abs video">
  <div class="frame" role="img" aria-label="Video still of an excited guest at a racing event"></div>
  <svg class="abs" style="left:90px;top:56px" width="40" height="30" aria-hidden="true"><rect width="40" height="30" rx="5" fill="rgba(0,0,0,.75)"/><polygon points="15,9 27,15 15,21" fill="#fff"/></svg>
  <div class="abs" style="left:0;top:140px;width:219px;height:2px;background:#c00"></div>
  <svg class="abs" style="left:8px;top:146px" width="60" height="10" aria-hidden="true"><polygon points="0,1 7,5 0,9" fill="#bbb"/><text x="42" y="8" font-size="6" fill="#bbb" font-family="Arial">0:00</text></svg>
</div>

<section class="abs card why">
  <h3 class="heading">Why consumer brands love plorvex</h3>
  <p>Turn live audiences into brand champions. Global consumer brands engage plorvex to leverage an asset they encounter at every event: attendees. Event guests have social network audiences who like and trust them. plorvex solutions facilitate participation and enable easy distribution of branded content to friends. Fun for guests. Amplification for brands.</p>
</section>

<aside class="abs card blog">
  <h3 class="heading">Social Blog</h3>
  <ul>
    <li class="current">What does Holmbrau do for Social Media Today? [Video Blog]</li>
    <li>Who is using Social Media? Young? Old? Both? Yes!</li>
    <li>Social Media World Forum Interview: Marit Dekkers-Vos of NLA</li>
    <li>RFID Connects Social Media to the Real World, Instantly</li>
    <li>Adding Experiential Social Media to Events [Video Interview - Korvane]</li>
  </ul>
</aside>

<div class="abs divider" style="top:920px"></div>
<div class="abs clients">
  <div class="client">Gamoro</div>
  <div class="client">Korvane</div>
  <div class="client">Cocobelle</div>
  <div class="client">dealnest</div>
</div>
<svg class="abs pager" viewBox="0 0 19 19" aria-hidden="true"><path d="M7 5l5 4.5-5 4.5" stroke="#fff" stroke-width="2" fill="none"/></svg>
<svg class="abs pager prev" viewBox="0 0 19 19" aria-hidden="true"><path d="M12 5l-5 4.5 5 4.5" stroke="#fff" stroke-width="2" fill="none"/></svg>
<div class="abs cta">plorvex is a Linkora preferred<br>marketing developer ››</div>
<div class="abs divider" style="top:1008px"></div>

<section class="abs foot" style="left:196px;top:1030px">
  <h4>Linkes</h4>
  <ul><li>Home</li><li>About Us</li><li>Solutions</li><li>Resource</li><li>Social Blog</li></ul>
</section>
<section class="abs foot follow" style="left:330px;top:1030px">
  <h4>Follow Us</h4>
  <ul><li>Follow Us on Chirply</li><li>Follow Us on Linkora</li><li>Follow Us on Netlinkr</li><li>Follow Us on Rss feeds</li></ul>
</section>
<section class="abs foot" style="left:523px;top:1030px">
  <h4>Quick Contact</h4>
  <p>Harbor Works Center,<br>Two Lantern Way,<br>9th Floor,<br>Fairhaven, MA 02719<br>Phone: 555-014-2290</p>
</section>
<section class="abs foot" style="left:704px;top:1030px;width:192px">
  <h4>Roving Photographer</h4>
  <p style="margin-top:4px">Fun and memorable experiences often occur in our lives when taking out a smart phone is awkward or not even an option. Guests shouldn't miss the best memories of their lives at your events just because they can't stop to take out a mobile device.</p>
</section>

<footer class="abs footer-bar">© Copyright 2013 plorvex</footer>
</body>
</html>
```